Weinetiketten für unsere neue Weinlinie SOMMERGLUT
Zielgruppe
Wir stellen qualitativ sehr hochwertige Weine, Sekte und Destillate her.
Unsere Zielgruppe sind kaufkräftige Kunden zwischen 25-70 Jahren.
Aufgabenstellung
Edel, schlicht und zeitlos soll das neue Etikett werden, nur leicht verspielt.
Mit hohem Wiedererkennungswert, da die Wein auch im Fachhandel (in Regalen) präsentiert werden. Der Name "Sommerglut" steht für expressive Weine voller Fruchtaromen und Düften.

```html
<!DOCTYPE html>
<html lang="de">
<head>
<meta charset="utf-8">
<title>KRANICH Sommerglut – Weinetikett</title>
<link rel="stylesheet" href="https://fonts.googleapis.com/css2?family=Belleza&display=swap">
<style>
  :root {
    --backdrop: #f2f2f2;
    --label-black: #0b0b0b;
    --panel-white: #ffffff;
    --gold: #a99561;
    --lime: #c5d32a;
    --ink: #1a1a1a;
  }
  html, body {
    margin: 0;
    padding: 0;
    width: 1200px;
    height: 3001px;
    overflow: hidden;
    background: var(--backdrop);
  }
  .canvas {
    position: relative;
    width: 1200px;
    height: 3001px;
    font-family: "Belleza", "Optima", sans-serif;
  }
  .label {
    position: absolute;
    left: 125px;
    top: 100px;
    width: 950px;
    height: 2800px;
    background: var(--label-black);
  }
  .label__panel {
    position: absolute;
    left: 95px;
    top: 220px;
    width: 775px;
    height: 2280px;
    background: var(--panel-white);
    overflow: hidden;
  }
  .brand-mark {
    position: absolute;
    left: 0;
    right: 0;
    top: 140px;
    text-align: center;
  }
  .brand-mark__dot {
    display: block;
    margin: 0 auto;
  }
  .brand-mark__name {
    margin-top: 70px;
    color: var(--gold);
    font-size: 64px;
    letter-spacing: 12px;
    line-height: 1;
  }
  .wine-name {
    position: absolute;
    left: 0;
    right: 0;
    top: 1100px;
    text-align: center;
    color: var(--gold);
    line-height: 1;
    white-space: nowrap;
  }
  .wine-name__house {
    font-size: 138px;
    letter-spacing: 2px;
  }
  .wine-name__line {
    margin-top: 26px;
    font-size: 84px;
    letter-spacing: 2px;
  }
  .divider {
    position: absolute;
    left: 55px;
    top: 1793px;
    width: 683px;
    height: 4px;
    background: var(--lime);
  }
  .varietal {
    position: absolute;
    left: 0;
    right: 0;
    top: 1930px;
    text-align: center;
    color: var(--ink);
  }
  .varietal__grape {
    font-size: 70px;
    line-height: 88px;
    letter-spacing: 2px;
  }
  .varietal__vintage {
    margin-top: 22px;
    font-size: 52px;
    letter-spacing: 3px;
  }
</style>
</head>
<body>
<div class="canvas">
  <div class="label">
    <div class="label__panel">
      <div class="brand-mark">
        <svg class="brand-mark__dot" width="360" height="360" viewBox="0 0 360 360" aria-hidden="true">
          <circle cx="180" cy="180" r="170" fill="var(--gold)"/>
        </svg>
        <div class="brand-mark__name">KRANICH</div>
      </div>
      <div class="wine-name">
        <div class="wine-name__house">KRANICH</div>
        <div class="wine-name__line">SOMMERGLUT</div>
      </div>
      <div class="divider"></div>
      <div class="varietal">
        <div class="varietal__grape">CABERNET<br>SAUVIGNON</div>
        <div class="varietal__vintage">2009</div>
      </div>
    </div>
  </div>
</div>
</body>
</html>
```